Modern, clean business card for Brightfield Optics

Updated business card with a modern look.

Logo on the front
Dr Tomas R Berkvist and Associates on the front.
Three locations on the back:
Ridgecrest Marketco
555-184-2039
48213 E Larkmoor Ave

Pinewell Marketco
555-706-3158
6104 W Tamberlin Ave

Fernbrook Terrace Marketco
555-932-4471
3870 S Quinmore Rd

Chatterly icon. www.brightfieldsight.example

Nice open white space on back for writing next appointment time.

Target Market(s)

Main target is female 25-50, but I would like broad appeal.

Industry/Entity Type

Healthcare

Contact Information for Business Card

Modern look

Font styles to use
Serif

Requirements
Must have
• Logo and Dr Tomas R Berkvist and Associates on front.
• 3 locations on back
• white space for noting next appointment

```html
<!DOCTYPE html>
<html lang="en">
<head>
<meta charset="utf-8">
<title>Brightfield Optics – Business Card</title>
<link href="https://fonts.googleapis.com/css2?family=PT+Sans:wght@400;700&display=swap" rel="stylesheet">
<style>
  :root {
    --navy: #13195e;
    --blue: #2a7df7;
    --link-blue: #1f5fd6;
    --cyan: #5fe8fb;
    --frame: #111111;
    --paper: #ffffff;
    --paper-cool: #f5f8fb;
    --tint: #c9dcf3;
  }
  * { margin: 0; padding: 0; box-sizing: border-box; }
  html, body {
    width: 1070px; height: 1200px; overflow: hidden;
    background: var(--paper);
    font-family: "PT Sans", sans-serif;
  }
  .canvas { position: relative; width: 1070px; height: 1200px; }

  .card {
    position: absolute;
    border: 3px solid var(--frame);
    overflow: hidden;
  }
  .card-front { left: 40px; top: 31px; width: 896px; height: 570px; background: var(--paper); }
  .card-back { left: 2px; top: 630px; width: 946px; height: 488px; background: var(--paper-cool); }

  .backdrop-texture { position: absolute; }
  .card-front .backdrop-texture {
    right: 0; bottom: 0; width: 70%; height: 60%;
    background: radial-gradient(ellipse at 80% 70%, rgba(201,220,243,0.55), rgba(255,255,255,0) 70%);
  }
  .card-back .backdrop-texture {
    right: 0; top: 0; width: 75%; height: 70%;
    background: radial-gradient(ellipse at 75% 20%, rgba(150,190,235,0.6), rgba(245,248,251,0) 70%);
  }

  .brand-name {
    position: absolute;
    font-weight: 700;
    color: var(--navy);
    white-space: nowrap;
    letter-spacing: -0.5px;
    line-height: 1;
  }
  .brand-tagline {
    position: absolute;
    font-weight: 700;
    color: var(--navy);
    white-space: nowrap;
    line-height: 1;
    transform: translateX(-50%);
  }
  .card-front .brand-name { left: 50%; transform: translateX(-50%); top: 334px; font-size: 60px; }
  .card-front .brand-tagline { left: 442px; top: 403px; font-size: 28px; }

  .practice-band { position: absolute; left: 0; top: 440px; width: 100%; height: 70px; }
  .practice-band svg { position: absolute; inset: 0; }
  .practice-name {
    position: absolute; left: 106px; top: 452px;
    font-size: 37px; color: var(--navy); white-space: nowrap;
  }

  .card-back .brand-name { left: 278px; transform: translateX(-50%); top: 160px; font-size: 36px; }
  .card-back .brand-tagline { left: 312px; top: 202px; font-size: 16px; }

  .contact-icons { position: absolute; left: 66px; top: 290px; display: flex; flex-direction: column; gap: 11px; }
  .contact-icons svg { display: block; width: 22px; height: 22px; }

  .location {
    position: absolute; top: 286px;
    text-align: center; color: var(--link-blue);
    font-size: 24px; line-height: 33px;
    transform: translateX(-50%); white-space: nowrap;
  }
  .location-ridgecrest { left: 233px; }
  .location-pinewell { left: 500px; }
  .location-fernbrook { left: 786px; }

  .web-line {
    position: absolute; left: 343px; top: 422px;
    display: flex; align-items: center; gap: 12px;
    color: var(--link-blue); font-size: 29px; letter-spacing: 0.5px; white-space: nowrap;
  }
  .social-dot { width: 26px; height: 26px; border-radius: 50%; background: var(--link-blue); }
</style>
</head>
<body>
<main class="canvas">

  <section class="card card-front" aria-label="Card front">
    <div class="backdrop-texture" role="img" aria-label="Soft pale blue geometric diamond pattern"></div>
    <div class="brand-name">Brightfield Optics</div>
    <div class="brand-tagline">ADVANCED EYE CARE</div>
    <div class="practice-band">
      <svg viewBox="0 0 890 70" preserveAspectRatio="none" aria-hidden="true">
        <rect x="0" y="0" width="890" height="70" fill="var(--blue)"/>
        <polygon points="0,0 660,0 718,70 0,70" fill="var(--paper)"/>
        <polygon points="0,0 655,0 712,70 0,70" fill="var(--cyan)"/>
      </svg>
    </div>
    <div class="practice-name">Dr Tomas R Berkvist and Associates</div>
  </section>

  <section class="card card-back" aria-label="Card back">
    <div class="backdrop-texture" role="img" aria-label="Soft blue geometric diamond pattern"></div>
    <div class="brand-name">Brightfield Optics</div>
    <div class="brand-tagline">ADVANCED EYE CARE</div>

    <div class="contact-icons" aria-hidden="true">
      <svg viewBox="0 0 24 24"><circle cx="12" cy="12" r="12" fill="var(--link-blue)"/><path d="M6.5 12.5 12 7.5l5.5 5M8.5 11v5.5h7V11" fill="none" stroke="#fff" stroke-width="1.8" stroke-linejoin="round"/></svg>
      <svg viewBox="0 0 24 24"><circle cx="12" cy="12" r="12" fill="var(--link-blue)"/><path d="M8.3 6.5c.6-.4 1.2-.3 1.5.3l1 2c.2.5.1 1-.3 1.3l-.8.6c.6 1.4 1.6 2.5 3 3.2l.7-.8c.4-.4.9-.5 1.3-.2l2 1.1c.6.3.7 1 .3 1.5-1 1.3-2.3 1.6-3.8.9-2.9-1.4-4.9-3.6-5.900-6.6-.4-1.4 0-2.5 1-3.3z" fill="#fff"/></svg>
      <svg viewBox="0 0 24 24"><circle cx="12" cy="12" r="12" fill="var(--link-blue)"/><path d="M12 5.5c-2.6 0-4.4 1.9-4.4 4.3 0 3.1 4.4 8 4.4 8s4.4-4.9 4.4-8c0-2.4-1.8-4.3-4.4-4.3z" fill="#fff"/><circle cx="12" cy="9.8" r="1.6" fill="var(--link-blue)"/></svg>
    </div>

    <div class="location location-ridgecrest">Ridgecrest Marketco<br>555-184-2039<br>48213 E Larkmoor Ave</div>
    <div class="location location-pinewell">Pinewell Marketco<br>555-706-3158<br>6104 W Tamberlin Ave</div>
    <div class="location location-fernbrook">Fernbrook Terrace Marketco<br>555-932-4471<br>3870 S Quinmore Rd</div>

    <div class="web-line">
      <span class="social-dot" aria-label="Chatterly"></span>
      <span>www.brightfieldsight.example</span>
    </div>
  </section>

</main>
</body>
</html>
```